Business Card Design Project 4 Construction Business

I am after a creative, but sleek and simple/ clean business card design. This design will form the basis of future items and might include a logo or simply a creative way to lay out the text of my company name 'kestrel ventures'
I like the simplicity of black and white however I would also be happy to see a splash of colour introduced somehow to give the text some interest and make it stand out.
I would like a double sided card.
I am young (ish!) and professional, offering construction and project management services, what I don't want is the traditional builders type card featuring a cheesy hammer/ saw image etc.
As the company name, kestrel ventures, suggests, we focus on working closely and collaboratively together, in synergy with all stakeholders involved in the projects that we undertake
Construction

```html
<!DOCTYPE html>
<html lang="en">
<head>
<meta charset="utf-8">
<title>Kestrel Ventures – Business Card</title>
<link rel="stylesheet" href="https://fonts.googleapis.com/css2?family=Marcellus&family=Open+Sans:wght@400;600&display=swap">
<style>
  :root {
    --backdrop: #d9dde0;
    --card-white: #ffffff;
    --card-black: #1c1c1e;
    --ink-dark: #4f5052;
    --ink-mid: #6d6e71;
    --mark-grey: #6a6c70;
    --rule-grey: #c9c9c9;
    --band-grey: #3a3a3c;
    --accent-blue: #1fa9dc;
    --web-light: #d6d6d6;
  }
  * { box-sizing: border-box; margin: 0; padding: 0; }
  html, body { width: 1200px; height: 960px; overflow: hidden; }
  body {
    background: var(--backdrop);
    font-family: "Open Sans", Arial, sans-serif;
    position: relative;
  }
  .card {
    position: absolute;
    left: 240px;
    width: 720px;
    height: 410px;
    border-radius: 20px;
    overflow: hidden;
    box-shadow: 0 6px 18px rgba(0,0,0,0.18);
  }
  /* ---------- front ---------- */
  .card-front { top: 50px; background: var(--card-white); }
  .holder-name {
    position: absolute; left: 62px; top: 50px;
    font-family: "Marcellus", Georgia, serif;
    font-size: 34px; color: var(--ink-dark); letter-spacing: 0.5px;
  }
  .holder-role {
    position: absolute; left: 62px; top: 96px;
    font-family: "Marcellus", Georgia, serif;
    font-size: 24px; color: var(--ink-dark);
  }
  .wordmark-front {
    position: absolute; right: 56px; top: 120px;
    text-align: right;
    font-family: "Open Sans", Arial, sans-serif;
    font-weight: 600; font-size: 38px; line-height: 1.05;
    letter-spacing: 3px; color: var(--mark-grey);
    text-transform: uppercase;
  }
  .divider {
    position: absolute; left: 62px; right: 56px; top: 232px;
    height: 2px; background: var(--rule-grey);
  }
  .address {
    position: absolute; left: 66px; top: 262px;
    font-family: "Marcellus", Georgia, serif;
    font-size: 24px; line-height: 1.3; color: var(--ink-dark);
  }
  .contacts {
    position: absolute; left: 296px; top: 252px;
    list-style: none;
  }
  .contacts li {
    display: flex; align-items: center; gap: 12px;
    font-size: 20px; color: var(--ink-mid); height: 31px;
  }
  .contacts svg { width: 16px; height: 16px; flex: none; }
  .contacts .at { color: var(--accent-blue); font-weight: 600; width: 16px; text-align: center; font-size: 18px; }
  .foot-band {
    position: absolute; left: 0; bottom: 0; width: 720px; height: 48px;
  }
  /* ---------- back ---------- */
  .card-back { top: 500px; background: var(--card-black); }
  .wordmark-back {
    position: absolute; right: 60px; top: 120px;
    text-align: right;
    font-family: "Open Sans", Arial, sans-serif;
    font-weight: 600; font-size: 52px; line-height: 1.05;
    letter-spacing: 5px; color: var(--mark-grey);
    text-transform: uppercase;
  }
  .web-back {
    position: absolute; right: 70px; top: 290px;
    font-family: "Marcellus", Georgia, serif;
    font-size: 22px; color: var(--web-light); letter-spacing: 0.5px;
  }
</style>
</head>
<body>

<section class="card card-front" aria-label="Card front">
  <h1 class="holder-name">OWEN HARTLEY</h1>
  <p class="holder-role">Director</p>
  <p class="wordmark-front">Kestrel<br>Ventures</p>
  <div class="divider"></div>
  <address class="address">12 Harbour<br>Lane Northbridge<br>NSW 2063</address>
  <ul class="contacts">
    <li>
      <svg viewBox="0 0 16 16" aria-hidden="true"><path d="M4 1.5 L6.5 4.5 L5 6.2 C5.8 8 7.8 10 9.8 11 L11.5 9.5 L14.5 12 L12.8 14.3 C7.5 14 2 8.5 1.7 3.2 Z" fill="var(--accent-blue)"/></svg>
      0400 123 456
    </li>
    <li><span class="at">@</span>owen@kestrelventures.com.au</li>
    <li>
      <svg viewBox="0 0 16 16" aria-hidden="true"><circle cx="8" cy="8" r="7" fill="var(--accent-blue)"/><g stroke="#fff" stroke-width="0.9" fill="none"><ellipse cx="8" cy="8" rx="3" ry="7"/><line x1="1" y1="8" x2="15" y2="8"/><line x1="2.2" y1="4.5" x2="13.8" y2="4.5"/><line x1="2.2" y1="11.5" x2="13.8" y2="11.5"/></g></svg>
      www.kestrelventures.com.au
    </li>
  </ul>
  <svg class="foot-band" viewBox="0 0 720 48" preserveAspectRatio="none" aria-hidden="true">
    <rect x="0" y="18" width="720" height="30" fill="var(--band-grey)"/>
    <polygon points="518,0 720,0 720,30 508,30" fill="var(--accent-blue)"/>
    <polygon points="508,30 518,0 522,0 512,30" fill="#ffffff"/>
  </svg>
</section>

<section class="card card-back" aria-label="Card back">
  <p class="wordmark-back">Kestrel<br>Ventures</p>
  <p class="web-back">www.kestrelventures.com.au</p>
</section>

</body>
</html>
```